We have developed a fully functional App called Corvalink. However, it requires a nicer GUI. You can see screenshots of our App on www.corvalink-example.com under "Tutorial". For those of you with Android, you can also install it. When you go to Corvalink-example.com, your phone will automatically redirect you to download. From there, you'll get a better idea of what our App looks like and how your design can make it way better. Please note we expect a design idea for most screens (there's about 8 screens) but do just one screen first and if you win, you can do the other 8 after.

Target Market(s)

People looking for dating / flirting

Industry/Entity Type

Android

Requirements
Must have
• sleek looking

```html
<!DOCTYPE html>
<html lang="en">
<head>
<meta charset="utf-8">
<title>Corvalink – Home</title>
<link href="https://fonts.googleapis.com/css2?family=Roboto:wght@300;400;500&display=swap" rel="stylesheet">
<style>
  :root {
    --page-bg: #d5e6e3;
    --system-bar: #000000;
    --teal: #2fc6ad;
    --teal-light: #45cfbc;
    --tab-bg: #f1f1f1;
    --tab-icon: #6b6b6b;
    --list-deep: #0d3a30;
    --list-mid: #2b6a5a;
    --card-bg: rgba(150, 165, 160, 0.32);
    --text-light: #ffffff;
    --text-soft: #e4eeeb;
    --avatar: #e8f1ef;
    --online: #2ec4a6;
    --offline: #e84444;
    --away: #f6902b;
  }
  * { box-sizing: border-box; margin: 0; padding: 0; }
  html, body {
    width: 882px; height: 1200px; overflow: hidden;
    background: var(--page-bg);
    font-family: 'Roboto', sans-serif;
  }
  .screen {
    position: absolute; left: 126px; top: 36px;
    width: 630px; height: 1128px;
    overflow: hidden; background: var(--list-deep);
  }
  .status-bar {
    height: 44px; background: var(--system-bar);
    display: flex; align-items: center; justify-content: flex-end;
    gap: 8px; padding-right: 16px; color: var(--text-light);
    font-size: 26px; font-weight: 400;
  }
  .status-bar .clock { margin-left: 6px; }
  .app-bar {
    height: 83px;
    background: linear-gradient(90deg, var(--teal-light), var(--teal));
    display: flex; align-items: center; padding: 0 24px;
    color: var(--text-light);
  }
  .app-bar .title { font-size: 31px; font-weight: 400; flex: 1; }
  .app-bar .actions { display: flex; gap: 34px; align-items: center; }
  .tabs {
    position: relative; height: 83px; background: var(--tab-bg);
    display: flex;
  }
  .tab { flex: 1; display: flex; align-items: center; justify-content: center; }
  .tab-indicator {
    position: absolute; left: 0; bottom: 0; width: 210px; height: 6px;
    background: var(--teal);
  }
  .member-list {
    position: relative; height: 826px; overflow: hidden;
    padding: 19px 19px 0;
    background:
      linear-gradient(125deg, transparent 30%, rgba(120, 200, 175, 0.25) 45%, transparent 60%),
      radial-gradient(ellipse at 70% 45%, var(--list-mid), var(--list-deep) 75%);
  }
  .member-card {
    position: relative; height: 177px; margin-bottom: 19px;
    background: var(--card-bg);
    box-shadow: 0 2px 4px rgba(0, 0, 0, 0.35);
    color: var(--text-light);
  }
  .avatar {
    position: absolute; left: 42px; top: 33px;
    width: 81px; height: 81px; border-radius: 50%;
    background: var(--avatar);
  }
  .status-badge {
    position: absolute; left: 23px; top: 120px;
    width: 80px; height: 22px; border-radius: 5px;
    font-size: 16px; font-weight: 400; letter-spacing: 0.5px;
    text-align: center; line-height: 22px; color: var(--text-light);
  }
  .status-badge.online { background: var(--online); }
  .status-badge.offline { background: var(--offline); }
  .status-badge.away { background: var(--away); }
  .member-name {
    position: absolute; left: 140px; top: 26px;
    font-size: 31px; font-weight: 400;
  }
  .member-tagline {
    position: absolute; left: 140px; top: 68px;
    font-size: 21px; font-weight: 300; color: var(--text-soft);
  }
  .member-location {
    position: absolute; left: 140px; top: 128px;
    display: flex; align-items: center; gap: 7px;
    font-size: 17px; font-weight: 400; color: var(--text-soft);
  }
  .chevron { position: absolute; right: 24px; top: 72px; }
  .nav-bar {
    height: 92px; background: var(--system-bar);
    display: flex; align-items: center; justify-content: space-around;
    padding: 0 40px;
  }
</style>
</head>
<body>
<main class="screen">
  <div class="status-bar">
    <svg width="30" height="24" viewBox="0 0 30 24" aria-hidden="true"><path d="M15 22 L1 7 A20 20 0 0 1 29 7 Z" fill="#fff"/></svg>
    <svg width="22" height="24" viewBox="0 0 22 24" aria-hidden="true"><path d="M2 22 L20 22 L20 2 Z" fill="#fff"/></svg>
    <svg width="14" height="26" viewBox="0 0 14 26" aria-hidden="true"><rect x="4" y="0" width="6" height="3" fill="#fff"/><rect x="0" y="3" width="14" height="23" rx="1" fill="#fff"/></svg>
    <span class="clock">12:06</span>
  </div>

  <header class="app-bar">
    <span class="title">Home</span>
    <div class="actions">
      <svg width="38" height="38" viewBox="0 0 38 38" aria-label="Search"><circle cx="15" cy="15" r="10" fill="none" stroke="#fff" stroke-width="3.5"/><line x1="22" y1="22" x2="34" y2="34" stroke="#fff" stroke-width="4.5" stroke-linecap="round"/></svg>
      <svg width="38" height="38" viewBox="0 0 38 38" aria-label="Profile"><circle cx="19" cy="19" r="16" fill="none" stroke="#fff" stroke-width="3"/><circle cx="19" cy="15" r="6" fill="#fff"/><path d="M8 30 Q19 17 30 30 Z" fill="#fff"/></svg>
    </div>
  </header>

  <nav class="tabs">
    <div class="tab"><svg width="36" height="34" viewBox="0 0 36 34" aria-label="Home"><path d="M18 2 L2 17 H7 V32 H15 V22 H21 V32 H29 V17 H34 Z" fill="var(--teal)"/></svg></div>
    <div class="tab"><svg width="38" height="34" viewBox="0 0 38 34" aria-label="Messages"><path d="M2 3 H24 V17 H10 L4 22 V17 H2 Z" fill="var(--tab-icon)"/><path d="M14 20 H28 V8 H36 V24 H34 V30 L28 24 H14 Z" fill="var(--tab-icon)"/></svg></div>
    <div class="tab"><svg width="36" height="36" viewBox="0 0 36 36" aria-label="Settings"><circle cx="18" cy="18" r="12" fill="none" stroke="var(--tab-icon)" stroke-width="6" stroke-dasharray="4.7 4.7"/><circle cx="18" cy="18" r="10" fill="var(--tab-icon)"/><circle cx="18" cy="18" r="4.5" fill="var(--tab-bg)"/></svg></div>
    <span class="tab-indicator"></span>
  </nav>

  <section class="member-list">
    <article class="member-card">
      <div class="avatar" role="img" aria-label="Member profile photo"></div>
      <span class="status-badge online">ONLINE</span>
      <h2 class="member-name">SweetGuy85, 29</h2>
      <p class="member-tagline">“Sweet, never sour!”</p>
      <p class="member-location"><svg width="11" height="16" viewBox="0 0 11 16" aria-hidden="true"><path d="M5.5 0 A5.5 5.5 0 0 1 11 5.5 C11 9 5.5 16 5.5 16 C5.5 16 0 9 0 5.5 A5.5 5.5 0 0 1 5.5 0 Z" fill="#fff"/><circle cx="5.5" cy="5.5" r="2" fill="#4a6a62"/></svg>Los Angeles, USA</p>
      <svg class="chevron" width="16" height="30" viewBox="0 0 16 30" aria-hidden="true"><path d="M2 2 L14 15 L2 28" fill="none" stroke="var(--teal)" stroke-width="2.5"/></svg>
    </article>

    <article class="member-card">
      <div class="avatar" role="img" aria-label="Member profile photo"></div>
      <span class="status-badge offline">OFFLINE</span>
      <h2 class="member-name">LookinAround, 24</h2>
      <p class="member-tagline">“Goddess &amp; Temptress lives here”</p>
      <p class="member-location"><svg width="11" height="16" viewBox="0 0 11 16" aria-hidden="true"><path d="M5.5 0 A5.5 5.5 0 0 1 11 5.5 C11 9 5.5 16 5.5 16 C5.5 16 0 9 0 5.5 A5.5 5.5 0 0 1 5.5 0 Z" fill="#fff"/><circle cx="5.5" cy="5.5" r="2" fill="#4a6a62"/></svg>Sacramento, USA</p>
      <svg class="chevron" width="16" height="30" viewBox="0 0 16 30" aria-hidden="true"><path d="M2 2 L14 15 L2 28" fill="none" stroke="var(--teal)" stroke-width="2.5"/></svg>
    </article>

    <article class="member-card">
      <div class="avatar" role="img" aria-label="Member profile photo"></div>
      <span class="status-badge online">ONLINE</span>
      <h2 class="member-name">MrLonely, 32</h2>
      <p class="member-tagline">“Looking forhappiness &amp; pleasure”</p>
      <p class="member-location"><svg width="11" height="16" viewBox="0 0 11 16" aria-hidden="true"><path d="M5.5 0 A5.5 5.5 0 0 1 11 5.5 C11 9 5.5 16 5.5 16 C5.5 16 0 9 0 5.5 A5.5 5.5 0 0 1 5.5 0 Z" fill="#fff"/><circle cx="5.5" cy="5.5" r="2" fill="#4a6a62"/></svg>Chicago, USA</p>
      <svg class="chevron" width="16" height="30" viewBox="0 0 16 30" aria-hidden="true"><path d="M2 2 L14 15 L2 28" fill="none" stroke="var(--teal)" stroke-width="2.5"/></svg>
    </article>

    <article class="member-card">
      <div class="avatar" role="img" aria-label="Member profile photo"></div>
      <span class="status-badge away">AWAY</span>
      <h2 class="member-name">JaneSants, 28</h2>
      <p class="member-tagline">“Smart, Kind &amp; Drama Free!”</p>
      <p class="member-location"><svg width="11" height="16" viewBox="0 0 11 16" aria-hidden="true"><path d="M5.5 0 A5.5 5.5 0 0 1 11 5.5 C11 9 5.5 16 5.5 16 C5.5 16 0 9 0 5.5 A5.5 5.5 0 0 1 5.5 0 Z" fill="#fff"/><circle cx="5.5" cy="5.5" r="2" fill="#4a6a62"/></svg>Los Angeles, USA</p>
      <svg class="chevron" width="16" height="30" viewBox="0 0 16 30" aria-hidden="true"><path d="M2 2 L14 15 L2 28" fill="none" stroke="var(--teal)" stroke-width="2.5"/></svg>
    </article>

    <article class="member-card"></article>
  </section>

  <footer class="nav-bar">
    <svg width="60" height="34" viewBox="0 0 60 34" aria-label="Back"><path d="M14 6 L4 14 L14 22 M4 14 H44 A9 9 0 0 1 44 32 H36" fill="none" stroke="#cfcfcf" stroke-width="3"/></svg>
    <svg width="64" height="34" viewBox="0 0 64 34" aria-label="Home"><path d="M4 30 L14 6 H50 L60 30 Z" fill="none" stroke="#cfcfcf" stroke-width="3"/></svg>
    <svg width="60" height="34" viewBox="0 0 60 34" aria-label="Recent apps"><path d="M12 10 V4 H56 V24 H50" fill="none" stroke="#cfcfcf" stroke-width="3"/><rect x="4" y="12" width="44" height="20" fill="none" stroke="#cfcfcf" stroke-width="3"/></svg>
  </footer>
</main>
</body>
</html>
```